Business Cards for a Junk Removal Company

Hello,
We are looking to have business cards designed that are simple, bold, easy to read, and right to the point. Please see the attachments for our logo files. We want the card to be yellow on both sides ( Color code Yellow: #FFE01B). The logo text font is (Rockstar Extra Bold) and this is also in the files attached. Please make the text black for the logo. On the back side of the card, you can use white and black for text. Thank you in advance for your hard work!

Front of card-
Harbor Haul Away (logo)
Back of card-
Harbor Haul Away
Donate - Recycle - Dispose
555-271-8093
www.harborhaulaway.example
info@harborhaulaway.example

Industry/Entity Type

Junk removal

Contact Information for Business Card

FRONT OF CARD- Harbor Haul Away (logo) BACK OF CARD- Harbor Haul Away Donate - Recycle - Dispose 555-271-8093 www.harborhaulaway.example info@harborhaulaway.example

Font styles to use
Other font styles liked:
• Rockstar Extra Bold

Colors
FFF300
FFF600
FEFA6F
FFFEC7
FFFEE8

Requirements
Must have
• Must have color code Yellow: #FFE01B for the background of front and back of the card

```html
<!DOCTYPE html>
<html lang="en">
<head>
<meta charset="UTF-8">
<title>Harbor Haul Away – Business Cards</title>
<link href="https://fonts.googleapis.com/css2?family=Anton&family=Teko:wght@600&display=swap" rel="stylesheet">
<style>
  :root {
    --stage: #d4d5d7;
    --card-yellow: #ffe01b;
    --ink: #000000;
  }
  * { margin: 0; padding: 0; box-sizing: border-box; }
  html, body {
    width: 900px;
    height: 1200px;
    overflow: hidden;
    background: var(--stage);
  }
  .sheet {
    position: relative;
    width: 900px;
    height: 1200px;
  }
  .card {
    position: absolute;
    left: 121px;
    width: 657px;
    height: 375px;
    background: var(--card-yellow);
    overflow: hidden;
  }
  .card--front { top: 204px; }
  .card--back  { top: 621px; }

  .wordmark {
    position: absolute;
    left: 0;
    right: 0;
    display: flex;
    flex-direction: column;
    align-items: center;
    color: var(--ink);
    font-family: "Anton", sans-serif;
    font-weight: 400;
    text-transform: uppercase;
    line-height: 0.95;
  }
  .wordmark__main { letter-spacing: 1px; }
  .wordmark__sub  { letter-spacing: 6px; }

  .card--front .wordmark { top: 118px; }
  .card--front .wordmark__main { font-size: 80px; }
  .card--front .wordmark__sub  { font-size: 40px; }

  .card--back .wordmark { top: 54px; }
  .card--back .wordmark__main { font-size: 66px; }
  .card--back .wordmark__sub  { font-size: 33px; letter-spacing: 5px; }

  .contact {
    position: absolute;
    top: 196px;
    left: 0;
    right: 0;
    display: flex;
    flex-direction: column;
    align-items: center;
    gap: 5px;
    list-style: none;
    font-family: "Teko", sans-serif;
    font-weight: 600;
    color: var(--ink);
    text-transform: uppercase;
    line-height: 1;
  }
  .contact__phone { font-size: 21px; letter-spacing: 7px; }
  .contact__email,
  .contact__web   { font-size: 20px; letter-spacing: 1px; }

  .services-band {
    position: absolute;
    top: 306px;
    left: 0;
    right: 0;
    height: 35px;
    background: var(--ink);
    color: var(--card-yellow);
    display: flex;
    align-items: center;
    justify-content: center;
    font-family: "Teko", sans-serif;
    font-weight: 600;
    font-size: 27px;
    letter-spacing: 2.5px;
    text-transform: uppercase;
    padding-top: 4px;
  }
</style>
</head>
<body>
<main class="sheet">
  <section class="card card--front" aria-label="Front of card">
    <div class="wordmark">
      <span class="wordmark__main">Harbor</span>
      <span class="wordmark__sub">Haul Away</span>
    </div>
  </section>

  <section class="card card--back" aria-label="Back of card">
    <div class="wordmark">
      <span class="wordmark__main">Harbor</span>
      <span class="wordmark__sub">Haul Away</span>
    </div>
    <ul class="contact">
      <li class="contact__phone">555-271-8093</li>
      <li class="contact__email">info@harborhaulaway.example</li>
      <li class="contact__web">www.harborhaulaway.example</li>
    </ul>
    <div class="services-band">Donate - Recycle - Dispose</div>
  </section>
</main>
</body>
</html>
```